A Flyer for a clinic/hospital waiting room to warn about patients that they must not abuse our staff

we need a flyer (text attached) with a background of a female nurse or medical doctor photo. I like the example photo where there are four headless satff lined up - something like this, indicating that we are a team and will not tolerate abuse
A4
the text will be over the photo.

Target Market(s)

patients who come to our clinic

Industry/Entity Type

medicine - urology

Colors
0054AA
0677BA
7BADD7
CADEEF
E8F1F8
0094D4
00A9DD
6FCCEA
C7EBF8
E9F6FB

Requirements
Must have
• a photo taking up the whole A4, and text over this. The photos I haev sent are just examples - I will need yo to source a photo
Nice to have
• Horizontal A4 and vertical A4 options. Please add our logo in small , in the bottom right corner

```html
<!DOCTYPE html>
<html lang="en">
<head>
<meta charset="utf-8">
<title>Zero-Tolerance Flyer</title>
<link href="https://fonts.googleapis.com/css2?family=Montserrat:wght@300;400;500;600;700&display=swap" rel="stylesheet">
<style>
  :root {
    --page-bg: #d9d9d9;
    --blue-deep: #0677BA;
    --blue-bright: #00A9DD;
    --blue-light: #C7EBF8;
    --band-dark: #262728;
    --band-mid: #48494b;
    --text-white: #ffffff;
    --text-soft: #c9cbce;
    --photo-light: #e9eef3;
    --photo-mid: #b9c6d3;
    --logo-ink: #2d3640;
  }
  * { margin: 0; padding: 0; box-sizing: border-box; }
  html, body {
    width: 1200px; height: 960px; overflow: hidden;
    background: var(--page-bg);
    font-family: "Montserrat", sans-serif;
  }
  .flyer {
    position: absolute; left: 40px; top: 84px;
    width: 1120px; height: 792px; overflow: hidden;
    box-shadow: 0 14px 40px rgba(0,0,0,0.25);
  }
  .flyer__photo {
    position: absolute; inset: 0;
    background: linear-gradient(120deg, var(--photo-mid) 0%, var(--photo-light) 45%, #f4f7fa 65%, #8fb3d6 100%);
  }
  .flyer__logo {
    position: absolute; right: 110px; top: 120px;
    font-weight: 600; font-size: 17px; color: var(--logo-ink);
  }
  .flyer__band {
    position: absolute; left: 0; right: 0; top: 440px; bottom: 0;
    background: linear-gradient(100deg, var(--band-dark) 0%, #333436 50%, var(--band-mid) 100%);
    opacity: 0.96;
  }
  .headline-box {
    position: absolute; left: 90px; top: 180px;
    width: 480px; border-radius: 12px;
    background: linear-gradient(160deg, var(--blue-bright) 0%, #2aa0d6 50%, var(--blue-deep) 100%);
    padding: 30px 34px 32px; color: var(--text-white);
  }
  .headline-box__kicker {
    font-weight: 300; font-size: 15px; color: var(--blue-light);
    margin-bottom: 12px;
  }
  .headline-box__title {
    font-weight: 700; font-size: 58px; line-height: 0.98;
    margin-bottom: 22px;
  }
  .headline-box__promise {
    font-weight: 500; font-size: 19px; line-height: 1.3;
  }
  .policy {
    position: absolute; left: 90px; right: 90px; top: 500px;
    color: var(--text-white);
  }
  .policy__heading {
    font-weight: 500; font-size: 27px; margin-bottom: 18px;
  }
  .policy__lists {
    display: flex; gap: 60px; margin-bottom: 22px;
  }
  .policy__list {
    list-style: none; flex: 1;
    font-weight: 700; font-size: 15px; line-height: 1.45;
  }
  .policy__list li::before { content: "• "; }
  .policy__notes p {
    font-weight: 300; font-size: 12.5px; line-height: 1.5;
    color: var(--text-soft); margin-bottom: 6px;
  }
</style>
</head>
<body>
  <main class="flyer">
    <div class="flyer__photo" role="img" aria-label="Photo of a medical team in white coats with stethoscopes, arms crossed, faces out of frame"></div>

    <div class="flyer__logo">Harbourview Clinic</div>

    <div class="flyer__band"></div>

    <section class="headline-box">
      <p class="headline-box__kicker">We have zero-tolerance for any form of</p>
      <h1 class="headline-box__title">Aggressive behaviour</h1>
      <p class="headline-box__promise">Our staff treat you with respect and we expect the same in return</p>
    </section>

    <section class="policy">
      <h2 class="policy__heading">Aggressive behaviour (in-person or on the telephone) is</h2>
      <div class="policy__lists">
        <ul class="policy__list">
          <li>Verbal harassment</li>
          <li>Any verbal or physical confrontation</li>
          <li>Raising your voice or making unreasonable demands</li>
        </ul>
        <ul class="policy__list">
          <li>Abusive or intimidating behaviour</li>
          <li>Sexual or suggestive language or behaviour</li>
          <li>Making threats to our staff</li>
          <li>Swearing</li>
        </ul>
      </div>
      <div class="policy__notes">
        <p>If any of our staff feel intimidated in any way, we will always support them. Incidents will result in your immediate removal from the facility, termination of your relationship with the practice, and may result in prosecution.</p>
        <p>In all circumstances we will support any staff member who wishes to press charges against a perpetrator of aggressive behaviour.</p>
        <p>We take this stance because our staff work extremely hard in busy circumstances to help you and we will no longer tolerate any form of aggression or abuse.</p>
      </div>
    </section>
  </main>
</body>
</html>
```